Storm Restoration Contractor needs a professional business card design

Looking for a professional business card design. Not looking for your cheapo MS Word standard ones that are readily available. Dont want it to be cookie cutter look like ones readily available online. We just recently changed our logo and want to freshen up all our documents. Our company handles restoring a property back to a pre-loss condition after a storm damages it. For example, wind, hail, flood, fire losses.

Target Market(s)

Property Owners, Homeowners, Property Owners, Commercial Property Owners, Property Management Companies, Hail and Wind Damaged Properties

Industry/Entity Type

Construction Company

Contact Information for Business Card

Brightline Facades
847-555-0193
847-555-0147 fax
www.brightlinefacades.example
info@brightlinefacades.example

Requirements
Must have
• Clean, Professional, fresh look
• Storm Restoration, Roofing, Siding, Windows
Nice to have
• If there is a way to incorporate storms that may be cool.

```html
<!DOCTYPE html>
<html lang="en">
<head>
<meta charset="utf-8">
<title>Brightline Facades – Business Card</title>
<link rel="stylesheet" href="https://fonts.googleapis.com/css2?family=Lato:wght@400;700;900&display=swap">
<style>
  :root {
    --brand-blue: #1f76c4;
    --back-blue: #1274bd;
    --slate: #58595b;
    --white: #ffffff;
    --stage: #222222;
  }
  * { margin: 0; padding: 0; box-sizing: border-box; }
  html, body { width: 1189px; height: 1200px; overflow: hidden; background: var(--stage); }
  body { position: relative; font-family: "Lato", sans-serif; }

  .card {
    position: absolute; left: 171px; width: 856px; height: 488px; overflow: hidden;
  }
  .card-front { top: 66px; background: var(--white); }
  .card-back { top: 626px; background: var(--back-blue); }

  /* front: brand lockup */
  .brand { position: absolute; left: 45px; top: 46px; display: flex; align-items: center; gap: 26px; }
  .brand-dot { width: 120px; height: 120px; border-radius: 50%; border: 14px solid var(--brand-blue); }
  .brand-rule { width: 3px; height: 140px; background: var(--brand-blue); }
  .brand-name {
    font-weight: 900; font-size: 50px; line-height: 1.02; color: var(--brand-blue);
    text-transform: uppercase; letter-spacing: 1px;
  }

  .name-band, .info-panel { position: absolute; left: 0; }
  .name-band {
    top: 234px; width: 650px; height: 47px; background: var(--brand-blue);
    clip-path: polygon(0 0, 100% 0, 92% 100%, 0 100%);
    display: flex; align-items: center; padding-left: 43px; color: var(--white);
  }
  .person-name { font-weight: 700; font-size: 29px; letter-spacing: 0.5px; }
  .person-role { font-size: 22px; margin-left: 8px; padding-left: 8px; border-left: 2px solid var(--white); line-height: 1.1; }

  .info-panel {
    top: 281px; width: 640px; height: 207px; background: var(--slate);
    clip-path: polygon(0 0, 100% 0, 78% 100%, 0 100%);
    padding: 14px 0 0 44px; color: var(--white); font-size: 22px; line-height: 1.25;
  }
  .address { margin-bottom: 6px; }
  .contact-list { list-style: none; }
  .contact-list li { display: flex; align-items: center; gap: 8px; height: 27px; }
  .contact-list svg { width: 24px; height: 24px; flex: none; }

  .accent-ring {
    position: absolute; left: 588px; top: 222px; width: 290px; height: 290px; border-radius: 50%;
    background: var(--white); border: 22px solid var(--brand-blue);
    box-shadow: 0 0 0 14px var(--white);
  }

  /* back */
  .faint-ring {
    position: absolute; left: 270px; top: 70px; width: 340px; height: 340px; border-radius: 50%;
    border: 36px solid rgba(255,255,255,0.05);
  }
  .back-title {
    position: absolute; top: 146px; width: 100%; text-align: center;
    font-weight: 900; font-size: 33px; letter-spacing: 2px; text-transform: uppercase; color: var(--white);
  }
  .service-icons { position: absolute; top: 218px; left: 238px; display: flex; gap: 16px; }
  .service-icon {
    width: 81px; height: 81px; border-radius: 50%; border: 3px solid var(--white);
    display: flex; align-items: center; justify-content: center;
  }
  .service-icon svg { width: 46px; height: 46px; }
  .service-list {
    position: absolute; top: 324px; width: 100%; text-align: center;
    font-size: 23px; color: var(--white);
  }
</style>
</head>
<body>

<section class="card card-front">
  <div class="brand">
    <div class="brand-dot"></div>
    <div class="brand-rule"></div>
    <div class="brand-name">Brightline<br>Facades</div>
  </div>

  <div class="accent-ring"></div>

  <div class="name-band">
    <span class="person-name">DANIEL HARLOW</span>
    <span class="person-role">Project Manager</span>
  </div>

  <div class="info-panel">
    <p class="address">410 W Meridian Ave, Suite 118<br>Lakefield, IL 60099</p>
    <ul class="contact-list">
      <li>
        <svg viewBox="0 0 24 24"><rect width="24" height="24" fill="#1f76c4"/><path d="M5 9c0-2 14-2 14 0v2h-4V9H9v2H5z M7 12h10l1 6H6z" fill="#fff"/></svg>
        847-555-0193
      </li>
      <li>
        <svg viewBox="0 0 24 24"><rect width="24" height="24" fill="#1f76c4"/><rect x="8" y="4" width="8" height="16" rx="1.5" fill="#fff"/><rect x="9.5" y="6" width="5" height="5" fill="#1f76c4"/></svg>
        847-555-0162
      </li>
      <li>
        <svg viewBox="0 0 24 24"><rect width="24" height="24" fill="#1f76c4"/><rect x="4" y="7" width="16" height="11" fill="#fff"/><path d="M4 7l8 6 8-6" stroke="#1f76c4" stroke-width="1.5" fill="none"/></svg>
        dharlow@brightlinefacades.example
      </li>
      <li>
        <svg viewBox="0 0 24 24"><rect width="24" height="24" fill="#1f76c4"/><circle cx="12" cy="12" r="7" fill="none" stroke="#fff" stroke-width="1.5"/><ellipse cx="12" cy="12" rx="3" ry="7" fill="none" stroke="#fff" stroke-width="1.2"/><path d="M5 12h14M6 9h12M6 15h12" stroke="#fff" stroke-width="1.2"/></svg>
        www.brightlinefacades.example
      </li>
    </ul>
  </div>
</section>

<section class="card card-back">
  <div class="faint-ring"></div>
  <h1 class="back-title">Brightline Facades</h1>

  <div class="service-icons">
    <div class="service-icon" aria-label="Storm">
      <svg viewBox="0 0 46 46" fill="none" stroke="#fff" stroke-width="3" stroke-linecap="round">
        <path d="M6 8h34M10 15h26M14 22h18M17 29h12M20 36h6M22 42h2"/>
      </svg>
    </div>
    <div class="service-icon" aria-label="Water">
      <svg viewBox="0 0 46 46"><path d="M23 6c5 9 8 13 8 18a8 8 0 0 1-16 0c0-5 3-9 8-18z" fill="#fff"/><ellipse cx="23" cy="38" rx="16" ry="4" fill="none" stroke="#fff" stroke-width="2"/></svg>
    </div>
    <div class="service-icon" aria-label="Fire damage">
      <svg viewBox="0 0 46 46"><path d="M23 6L4 22h5v18h28V22h5z" fill="#fff"/><path d="M16 38c-3-3-2-8 2-11 0 3 2 4 3 4 0-4 2-7 5-9-1 4 3 6 3 10s-3 6-6 6z" fill="#1274bd"/></svg>
    </div>
    <div class="service-icon" aria-label="Commercial building">
      <svg viewBox="0 0 46 46" fill="#fff"><rect x="8" y="10" width="16" height="30"/><rect x="26" y="18" width="12" height="22"/><rect x="4" y="39" width="38" height="3"/><g fill="#1274bd"><rect x="11" y="14" width="3" height="3"/><rect x="17" y="14" width="3" height="3"/><rect x="11" y="21" width="3" height="3"/><rect x="17" y="21" width="3" height="3"/><rect x="11" y="28" width="3" height="3"/><rect x="17" y="28" width="3" height="3"/><rect x="29" y="23" width="2" height="3"/><rect x="33" y="23" width="2" height="3"/><rect x="29" y="30" width="2" height="3"/><rect x="33" y="30" width="2" height="3"/></g></svg>
    </div>
  </div>

  <p class="service-list">Storm Restoration | Roofing | Siding | Windows</p>
</section>

</body>
</html>
```